Business Card Design

I'm after a modern and artistic business card design, with clean lines and popping colour. The business card should be professional looking and promote my business.

```html
<!DOCTYPE html>
<html lang="en">
<head>
<meta charset="utf-8">
<title>Lorem Ipsum – Makeup Artist Business Card</title>
<link rel="stylesheet" href="https://fonts.googleapis.com/css2?family=Dancing+Script:wght@600&family=Questrial&display=swap">
<style>
  :root {
    --page-bg: #ece9e6;
    --card-black: #141414;
    --card-black-light: #2a2a2a;
    --card-white: #ffffff;
    --card-white-shade: #e6e6e6;
    --accent-pink: #e8246b;
    --text-light: #f4f4f4;
    --product-dark: #1d1a1e;
    --product-rose: #c4607a;
  }
  * { box-sizing: border-box; margin: 0; padding: 0; }
  html, body { width: 1200px; height: 800px; overflow: hidden; }
  body {
    background: var(--page-bg);
    display: flex;
    align-items: center;
    justify-content: center;
    gap: 40px;
    font-family: "Questrial", "Century Gothic", sans-serif;
  }
  .card {
    position: relative;
    width: 540px;
    height: 310px;
    overflow: hidden;
    box-shadow: 0 8px 24px rgba(0,0,0,0.18);
  }

  /* Front */
  .card-front {
    background: radial-gradient(ellipse at 70% 20%, var(--card-black-light), var(--card-black) 70%);
  }
  .name-band {
    position: absolute;
    left: 0; top: 98px;
    width: 238px; height: 36px;
    background: var(--accent-pink);
    display: flex; align-items: center;
    padding-left: 28px;
  }
  .name-band .name {
    font-family: "Dancing Script", cursive;
    font-size: 30px;
    color: var(--card-white);
    line-height: 1;
  }
  .role {
    position: absolute;
    left: 0; top: 140px;
    width: 238px;
    text-align: right;
    padding-right: 4px;
    color: var(--accent-pink);
    font-size: 15px;
    letter-spacing: 0.3px;
  }
  .product-photo {
    position: absolute;
    left: 350px; top: 62px;
    width: 150px; height: 150px;
    background:
      radial-gradient(circle at 30% 70%, var(--product-rose) 0 18%, transparent 19%),
      radial-gradient(circle at 75% 80%, var(--accent-pink) 0 12%, transparent 13%),
      linear-gradient(160deg, transparent 40%, var(--product-dark) 100%);
  }
  .contact {
    position: absolute;
    left: 80px; top: 222px;
    list-style: none;
    color: var(--text-light);
    font-size: 14.5px;
    line-height: 20px;
    letter-spacing: 0.3px;
  }
  .contact li:nth-child(2) { padding-left: 6px; }
  .contact li:nth-child(3) { padding-left: 12px; }

  /* Back */
  .card-back {
    background: radial-gradient(ellipse at 50% 45%, var(--card-white) 40%, var(--card-white-shade) 100%);
  }
  .stripe {
    position: absolute;
    height: 22px;
    background: var(--accent-pink);
  }
  .stripe-left { left: 0; top: 122px; width: 170px; }
  .stripe-right { right: 0; top: 170px; width: 200px; }
  .back-name {
    position: absolute;
    left: 175px; top: 128px;
    font-family: "Dancing Script", cursive;
    font-size: 38px;
    color: var(--accent-pink);
    letter-spacing: 1px;
    line-height: 1;
  }
</style>
</head>
<body>
  <section class="card card-front">
    <div class="name-band"><span class="name">Lorem Ipsum</span></div>
    <p class="role">Makeup Artist</p>
    <div class="product-photo" role="img" aria-label="Photo of makeup products: lip liner pencil, lipstick, blush compact and loose powder"></div>
    <ul class="contact">
      <li>+61 4000 5218</li>
      <li>artist@rosalinestudio.com</li>
      <li>www.rosalinestudio.com</li>
    </ul>
  </section>

  <section class="card card-back">
    <div class="stripe stripe-left"></div>
    <p class="back-name">Lorem Ipsum</p>
    <div class="stripe stripe-right"></div>
  </section>
</body>
</html>
```